Business Card design for Recruiter providing Recruitment Staff Augmentation services

I need a double sided business card. I have used Plix to print cards in the past and really like their quality. I have a logo but need to change the tagline that is part of the graphic.

The tagline currently reads and Connnecting people with careers - but it should be removed.

The back should look like a notecard for writing a to do list with the first to-do Augment Recruiting Staff

```html
<!DOCTYPE html>
<html lang="en">
<head>
<meta charset="utf-8">
<title>Talent Summit – Business Card</title>
<link href="https://fonts.googleapis.com/css2?family=Arimo:wght@400;700&family=Montserrat:wght@400&display=swap" rel="stylesheet">
<style>
  :root {
    --backdrop: #3a322e;
    --card: #141517;
    --card-edge: #0c0d0e;
    --rule: #8a8d92;
    --blue: #2f77a8;
    --accent: #d6492c;
    --text: #f1f1f1;
    --muted: #7d8085;
  }
  * { box-sizing: border-box; margin: 0; padding: 0; }
  html, body { width: 1200px; height: 864px; overflow: hidden; }
  body {
    background: var(--backdrop);
    display: flex;
    align-items: center;
    justify-content: center;
    gap: 60px;
    font-family: "Arimo", Arial, sans-serif;
  }
  .card {
    position: relative;
    width: 540px;
    height: 309px;
    background: var(--card);
    border: 1px solid var(--card-edge);
    box-shadow: 0 14px 30px rgba(0,0,0,.45);
    overflow: hidden;
  }

  /* Back: notecard */
  .note-lines {
    position: absolute;
    left: 40px;
    right: 40px;
    top: 62px;
  }
  .note-lines span {
    display: block;
    height: 1px;
    background: var(--rule);
    opacity: .7;
    margin-bottom: 42px;
  }
  .back-mark {
    position: absolute;
    top: 22px;
    right: 40px;
    width: 30px;
    height: 30px;
    border-radius: 50%;
    background: #1b1c1f;
    box-shadow: inset 1px 1px 2px rgba(0,0,0,.7), inset -1px -1px 1px rgba(255,255,255,.06);
  }
  .back-web {
    position: absolute;
    left: 40px;
    bottom: 26px;
    font-size: 12px;
    letter-spacing: 5px;
    color: var(--muted);
  }

  /* Front */
  .brand {
    position: absolute;
    left: 34px;
    top: 128px;
    display: flex;
    align-items: center;
    gap: 8px;
  }
  .brand-dot {
    width: 18px;
    height: 18px;
    border-radius: 50%;
    background: var(--accent);
  }
  .brand-name {
    font-family: "Montserrat", Arial, sans-serif;
    font-weight: 400;
    font-size: 25px;
    letter-spacing: 1px;
    color: var(--blue);
    text-transform: uppercase;
  }
  .divider {
    position: absolute;
    left: 318px;
    top: 40px;
    width: 1px;
    height: 230px;
    background: linear-gradient(to bottom, transparent, #c9ccd0 40%, #c9ccd0 60%, transparent);
  }
  .contact {
    position: absolute;
    left: 338px;
    top: 52px;
    color: var(--text);
    font-size: 13px;
    line-height: 1.45;
  }
  .person-name { color: var(--blue); font-size: 18px; line-height: 1.1; }
  .person-role { color: var(--accent); font-size: 14px; margin-bottom: 10px; }
  .address { margin-bottom: 8px; }
  .contact-row { display: flex; align-items: center; gap: 8px; }
  .contact-row svg { width: 11px; height: 11px; fill: var(--blue); flex: none; }
  .contact-row .blank { width: 11px; flex: none; }
</style>
</head>
<body>

  <section class="card card-back" aria-label="Card back, notecard">
    <div class="back-mark"></div>
    <div class="note-lines"><span></span><span></span><span></span><span></span></div>
    <div class="back-web">www.talentsummit.com</div>
  </section>

  <section class="card card-front" aria-label="Card front">
    <div class="brand">
      <div class="brand-dot"></div>
      <div class="brand-name">Talent Summit</div>
    </div>
    <div class="divider"></div>
    <div class="contact">
      <div class="person-name">Evan Rourke</div>
      <div class="person-role">President</div>
      <div class="address">2719 Linden Court<br>Maple Ridge, NY 11420</div>
      <div class="contact-row">
        <svg viewBox="0 0 12 12"><path d="M2 1h3l1 3-2 1a7 7 0 0 0 3 3l1-2 3 1v3c-6 0-9-3-9-9z"/></svg>
        <span>555 0142 7781</span>
      </div>
      <div class="contact-row">
        <svg viewBox="0 0 12 12"><rect x="3" y="0" width="6" height="12" rx="1"/></svg>
        <span>555 0198 3364</span>
      </div>
      <div class="contact-row">
        <svg viewBox="0 0 12 12"><rect x="1" y="4" width="10" height="7"/><rect x="3" y="1" width="6" height="3"/></svg>
        <span>555 0176 2209</span>
      </div>
      <div class="contact-row">
        <svg viewBox="0 0 12 12"><rect x="0" y="2" width="12" height="8" rx="1"/></svg>
        <span>evan@talentsummit.com</span>
      </div>
      <div class="contact-row">
        <svg viewBox="0 0 12 12"><circle cx="6" cy="6" r="6"/></svg>
        <span>www.talentsummit.com</span>
      </div>
    </div>
  </section>

</body>
</html>
```